*** Business Card Design Project

I need a logo and business card for my new catering business: "Pomelia". The design should be modern, clean, elegant and refined. One or Two colours only. The design SHOULD NOT include graphics or images. There should be space for my name, phone number and email address (I will provide these to you later).

Industry/Entity Type

Catering

Requirements
Must have
• Must have one or two colours only.
Must include the text "pomelia"
Should not have
• Must not have graphics or images.

```html
<!DOCTYPE html>
<html lang="en">
<head>
<meta charset="utf-8">
<title>Pomelia — Business Card</title>
<link rel="stylesheet" href="https://fonts.googleapis.com/css2?family=Questrial&display=swap">
<style>
  :root {
    --backdrop: #333436;
    --card: #ffffff;
    --ink: #666666;
    --ink-soft: #6e6e6e;
  }
  html, body {
    margin: 0;
    padding: 0;
    width: 1200px;
    height: 1200px;
    overflow: hidden;
    background: var(--backdrop);
  }
  .stage {
    position: relative;
    width: 1200px;
    height: 1200px;
  }
  .card {
    position: absolute;
    top: 443px;
    width: 521px;
    height: 312px;
    background: var(--card);
    box-shadow: 4px 6px 12px rgba(0, 0, 0, 0.35);
  }
  .card--front { left: 54px; }
  .card--back  { left: 624px; }
  .card svg {
    display: block;
    width: 521px;
    height: 312px;
  }
  .card text {
    font-family: "Questrial", "Century Gothic", sans-serif;
    fill: var(--ink);
  }
  .wordmark { font-size: 34px; letter-spacing: 0.5px; }
  .phone { font-size: 16px; fill: var(--ink-soft); }
  .bullet { fill: var(--ink); }
  .holder-name { font-size: 18px; }
  .holder-role { font-size: 14px; }
  .address { font-size: 15px; }
  .web { font-size: 15px; }
</style>
</head>
<body>
<main class="stage">
  <section class="card card--front" aria-label="Card front">
    <svg viewBox="0 0 521 312" xmlns="http://www.w3.org/2000/svg">
      <text class="wordmark" x="260.5" y="165" text-anchor="middle">POMELIA</text>
      <text class="phone" x="39" y="271">+63 917 5550182</text>
      <circle class="bullet" cx="200.5" cy="265" r="2.6"/>
      <text class="phone" x="228" y="271">(083) 555019</text>
      <circle class="bullet" cx="354" cy="265" r="2.6"/>
      <text class="phone" x="382" y="271">(083) 5550147</text>
    </svg>
  </section>

  <section class="card card--back" aria-label="Card back">
    <svg viewBox="0 0 521 312" xmlns="http://www.w3.org/2000/svg">
      <text class="holder-name" x="260.5" y="103" text-anchor="middle">Mara LIND</text>
      <text class="holder-role" x="260.5" y="122" text-anchor="middle">Director</text>
      <text class="address" x="260.5" y="173" text-anchor="middle">dummy  dummy</text>
      <text class="address" x="260.5" y="192" text-anchor="middle">dummy dummy City dummy</text>
      <text class="web" x="260.5" y="221" text-anchor="middle">mara@pomelia.com  |  www.pomelia.com</text>
    </svg>
  </section>
</main>
</body>
</html>
```